Clinical Research Company Flyer

I have a mock version of the flyer here but we were unhappy with it, we want for it to look more balanced feel, we would like to add a qr code that points to bwmoq.com here is the link to the canva document if you would like to pull images or edit there https://www.plomira.net/design/KRWHOBmLVEZ/8_qYpRsTjLmW3xHfDgBvNZ/edit?utm_content=KRWHOBmLVEZ&utm_campaign=designshare&utm_medium=link2&utm_source=sharebutton

```html
<!DOCTYPE html>
<html lang="en">
<head>
<meta charset="utf-8">
<title>Our Mission — Bluebonnet Clinical Trials</title>
<link rel="stylesheet" href="https://fonts.googleapis.com/css2?family=Alegreya+Sans:wght@800&family=Belleza&display=swap">
<style>
  :root {
    --sky: #9cc6d8;
    --teal: #55c6d1;
    --deep-teal: #0b7398;
    --harbor: #1a7c92;
    --panel-grey: #8a8d91;
    --navy: #154e80;
    --ink: #1f2226;
    --mist-top: #d6e9f1;
    --mist-bottom: #e3e9f1;
    --white: #ffffff;
    --badge-navy: #1c4a6b;
    --badge-gold: #d9a633;
    --badge-red: #d2383b;
    --badge-light: #4cb2e0;
  }
  * { margin: 0; padding: 0; box-sizing: border-box; }
  html, body { width: 927px; height: 1200px; overflow: hidden; background: var(--white); }
  .flyer {
    position: relative;
    width: 927px;
    height: 1200px;
    overflow: hidden;
    font-family: "Belleza", "Optima", sans-serif;
    color: var(--ink);
  }
  .backdrop { position: absolute; inset: 0; }
  .credential-rail {
    position: absolute;
    left: 68px; top: 0;
    width: 250px; height: 1200px;
    background: var(--panel-grey);
  }
  .credential-rail svg { position: absolute; inset: 0; }
  .content-panel {
    position: absolute;
    left: 318px; top: 110px;
    width: 541px; height: 1090px;
    background: linear-gradient(to bottom, rgba(214,233,241,0) 0%, var(--mist-top) 12%, #edf6f9 35%, var(--mist-bottom) 100%);
  }
  .panel-stripe { position: absolute; inset: 0; pointer-events: none; }
  .skyline-faint {
    position: absolute;
    left: 318px; top: 760px;
    width: 541px; height: 380px;
    background: linear-gradient(to bottom, rgba(255,255,255,0) 0%, rgba(255,255,255,0.55) 45%, rgba(255,255,255,0.2) 100%);
  }
  .skyline-left {
    position: absolute; left: 0; top: 725px;
    width: 68px; height: 475px;
    background: linear-gradient(to bottom, var(--harbor), #1e7490);
  }
  .skyline-right {
    position: absolute; left: 894px; top: 742px;
    width: 33px; height: 458px;
    background: var(--deep-teal);
  }
  .tagline, .mission-title {
    position: absolute;
    right: 109px;
    text-align: right;
    font-family: "Alegreya Sans", "Optima", sans-serif;
    font-weight: 800;
    color: var(--navy);
  }
  .tagline {
    top: 138px;
    font-size: 33px;
    line-height: 37px;
    letter-spacing: 0.3px;
  }
  .mission-title {
    top: 262px;
    font-size: 66px;
    line-height: 58px;
  }
  .mission-copy {
    position: absolute;
    left: 363px; top: 461px;
    width: 455px;
    font-size: 19.5px;
    line-height: 30.3px;
    letter-spacing: -0.1px;
  }
  .mission-copy p + p { margin-top: 30.3px; }
  .mission-copy .line {
    display: block;
    text-align: justify;
    text-align-last: justify;
  }
  .mission-copy .line.last { text-align: left; text-align-last: left; }
  .site-qr {
    position: absolute;
    left: 363px; top: 998px;
    display: flex; flex-direction: column; align-items: center;
  }
  .qr-slot {
    width: 110px; height: 110px;
    background: var(--white);
    border: 2px solid var(--navy);
    border-radius: 4px;
  }
  .qr-caption {
    margin-top: 12px;
    font-size: 12px;
    letter-spacing: 0.6px;
    color: var(--ink);
  }
  .brand-mark {
    position: absolute;
    right: 109px; top: 998px;
    display: flex; flex-direction: column; align-items: flex-end;
  }
  .brand-dot {
    width: 110px; height: 110px;
    border-radius: 50%;
    background: var(--harbor);
    margin-bottom: 12px;
    margin-right: 6px;
  }
  .brand-name { font-size: 12px; color: var(--ink); letter-spacing: 0.2px; }
</style>
</head>
<body>
<main class="flyer">
  <svg class="backdrop" width="927" height="1200" viewBox="0 0 927 1200" aria-hidden="true">
    <rect width="927" height="1200" fill="var(--sky)"/>
    <polygon points="0,0 382,0 0,120" fill="var(--white)"/>
    <polygon points="0,498 927,205 927,1200 0,1200" fill="var(--teal)"/>
    <line x1="0" y1="490" x2="927" y2="197" stroke="var(--white)" stroke-width="9"/>
  </svg>

  <div class="skyline-left" role="img" aria-label="Dark teal city skyline silhouette"></div>
  <div class="skyline-right" role="img" aria-label="Tall dark blue tower of the city skyline"></div>

  <aside class="credential-rail" aria-label="Certifications and memberships">
    <svg width="250" height="1200" viewBox="68 0 250 1200">
      <polygon points="192,126 240,150 240,204 192,228 144,204 144,150" fill="var(--white)" stroke="var(--badge-red)" stroke-width="3" stroke-linejoin="round"/>
      <circle cx="192" cy="318" r="40" fill="#c4c6c9" opacity="0.7"/>
      <rect x="112" y="408" width="164" height="46" rx="6" fill="#1f4e8c"/>
      <rect x="118" y="496" width="150" height="42" rx="21" fill="#2a5a8a"/>
      <rect x="112" y="584" width="158" height="52" rx="6" fill="#3f7f4a" opacity="0.85"/>
      <circle cx="138" cy="737" r="48" fill="var(--badge-navy)"/>
      <circle cx="138" cy="737" r="34" fill="var(--panel-grey)"/>
      <circle cx="254" cy="737" r="48" fill="var(--badge-navy)"/>
      <circle cx="138" cy="854" r="48" fill="var(--badge-navy)"/>
      <circle cx="138" cy="854" r="34" fill="var(--panel-grey)"/>
      <circle cx="254" cy="854" r="48" fill="var(--badge-gold)"/>
      <circle cx="254" cy="854" r="42" fill="var(--badge-navy)"/>
      <rect x="104" y="938" width="76" height="86" rx="10" fill="#7a4fb0" opacity="0.85"/>
      <path d="M216,944 L286,944 L286,988 Q286,1010 251,1022 Q216,1010 216,988 Z" fill="#3d3f42" stroke="var(--white)" stroke-width="3"/>
      <circle cx="138" cy="1095" r="44" fill="var(--badge-light)"/>
      <circle cx="248" cy="1095" r="44" fill="none" stroke="#a3a6aa" stroke-width="3"/>
    </svg>
  </aside>

  <section class="content-panel" aria-hidden="true"></section>
  <svg class="panel-stripe" width="927" height="1200" viewBox="0 0 927 1200" aria-hidden="true">
    <line x1="318" y1="396" x2="927" y2="198" stroke="var(--white)" stroke-width="9"/>
  </svg>
  <div class="skyline-faint" role="img" aria-label="Faint white city skyline behind the mission text"></div>

  <h2 class="tagline">PROVIDING QUALITY DATA,<br>THROUGH TRUSTED CARE.</h2>
  <h1 class="mission-title">OUR<br>MISSION</h1>

  <div class="mission-copy">
    <p>
      <span class="line">We are a stand-alone clinical trials site conducting</span>
      <span class="line">medication and device trials. Comprised of expe-</span>
      <span class="line">rienced and dedicated staff, we collectively have</span>
      <span class="line">decades of experience in pharmaceutical drug</span>
      <span class="line">trials ranging from phase I-IV in the Dallas-Fort</span>
      <span class="line last">Worth metroplex.</span>
    </p>
    <p>
      <span class="line">We take patient safety as our primary concern, as</span>
      <span class="line">we believe that well-informed clinical trial volun-</span>
      <span class="line last">teers make the best clinical trials participants.</span>
    </p>
    <p>
      <span class="line">Our mission is to maximize the time we have on</span>
      <span class="line">each trial, bringing innovations to life with rapid</span>
      <span class="line">recruitment of the right participants and providing</span>
      <span class="line last">trusted data.</span>
    </p>
  </div>

  <div class="site-qr">
    <div class="qr-slot" role="img" aria-label="QR code linking to bwmoq.com"></div>
    <span class="qr-caption">bwmoq.com</span>
  </div>

  <div class="brand-mark">
    <span class="brand-dot" aria-hidden="true"></span>
    <span class="brand-name">Bluebonnet Clinical Trials</span>
  </div>
</main>
</body>
</html>
```